Surface Protection company needs cards

We are a New Zealand company that will apply nanotechnology coatings on surfaces to prevent growth and spread of bacteria, viruses, mold etc with a sprayer. We deal with large corporates, airlines, hospitals and schools so we are after a new modern, simple and clean look that will have great visual impact.
We a company that is focused on prevention and protection.

Company name, Vela Shield

Subtext, Antimicrobial Surface Protection

Logo, VS

Target Market(s)

Hospitals, Transport agencies, Airlines, Corporate entities

Contact Information for Business Card

Company name, VelaShield
Logo, VS

Gareth Tolley
velashieldnz@postbox.example
+64219305562
www.velashield.example.nz

Requirements
Must have
• Simple clean look.
Nice to have
• We apply nano coatings so try and incorporate this into a theme somehow

```html
<!DOCTYPE html>
<html lang="en">
<head>
<meta charset="utf-8">
<title>VelaShield Business Cards</title>
<link rel="stylesheet" href="https://fonts.googleapis.com/css2?family=Questrial&display=swap">
<style>
  :root {
    --bg: #141414;
    --card: #232323;
    --card-edge: #2c2c2c;
    --teal: #2fc0b3;
    --light: #d9d9d9;
    --muted: #bdbdbd;
  }
  * { margin: 0; padding: 0; box-sizing: border-box; }
  html, body {
    width: 1200px;
    height: 900px;
    overflow: hidden;
    background: var(--bg);
    font-family: "Questrial", "Century Gothic", sans-serif;
  }
  .canvas {
    width: 1200px;
    height: 900px;
    display: flex;
    flex-direction: column;
    align-items: center;
    justify-content: center;
    gap: 56px;
  }
  .card {
    position: relative;
    width: 600px;
    height: 343px;
    background: var(--card);
    border: 1px solid var(--card-edge);
    border-radius: 20px;
    box-shadow: 0 18px 40px rgba(0,0,0,0.55);
  }
  .brand {
    display: flex;
    align-items: center;
    gap: 14px;
    color: var(--teal);
    font-weight: 400;
    letter-spacing: -0.5px;
  }
  .brand-dot {
    border: 3px solid var(--light);
    border-radius: 50%;
    flex: none;
  }
  .card-front {
    display: flex;
    flex-direction: column;
    align-items: center;
    justify-content: center;
    gap: 22px;
  }
  .card-front .brand { font-size: 66px; }
  .card-front .brand-dot { width: 34px; height: 34px; }
  .tagline {
    color: var(--light);
    font-size: 19px;
    letter-spacing: 1.5px;
  }
  .card-back .brand {
    position: absolute;
    top: 70px;
    right: 70px;
    font-size: 52px;
  }
  .card-back .brand-dot { width: 28px; height: 28px; }
  .details {
    position: absolute;
    left: 46px;
    bottom: 58px;
    display: flex;
    align-items: center;
    gap: 18px;
  }
  .person { text-align: left; }
  .person-name {
    color: var(--muted);
    font-size: 19px;
    letter-spacing: 3px;
    text-transform: uppercase;
  }
  .person-role {
    color: var(--teal);
    font-size: 15px;
    letter-spacing: 1.5px;
    margin-top: 2px;
  }
  .divider {
    width: 2px;
    height: 62px;
    background: var(--teal);
  }
  .contact {
    list-style: none;
    color: var(--light);
    font-size: 15px;
    letter-spacing: 1px;
    line-height: 1.65;
  }
  .contact .accent { color: var(--teal); }
</style>
</head>
<body>
  <main class="canvas">
    <section class="card card-front" aria-label="Card front">
      <div class="brand"><span class="brand-name">VelaShield</span><span class="brand-dot"></span></div>
      <p class="tagline">Antimicrobial Surface Protection</p>
    </section>

    <section class="card card-back" aria-label="Card back">
      <div class="brand"><span class="brand-name">VelaShield</span><span class="brand-dot"></span></div>
      <div class="details">
        <div class="person">
          <p class="person-name">Gareth Tolley</p>
          <p class="person-role">Managing Director</p>
        </div>
        <span class="divider"></span>
        <ul class="contact">
          <li>+64 219 305 562</li>
          <li>velashieldnz@postbox.example</li>
          <li>www.<span class="accent">velashield</span>.example.nz</li>
        </ul>
      </div>
    </section>
  </main>
</body>
</html>
```